New business card design

I need original, modern, business looking but dzen (minimalistic) looking design.
Also refer to websit trevanix.ru

Text is

Дробышев Кирилл, PMP
Партнер

Моб. +7 (915) 460 7185
info@trevanix.ru
Москва, Россия, 117342, ул. Береговая 7/2
=====================

Drobyshev Kirill, PMP
Partner

Mob. +7 (915) 460 7185
info@trevanix.ru
Moscow, Russia,117342, Beregovaya 7/2

Industry/Entity Type

Business

Font styles to use
Serif
Sans Serif

```html
<!DOCTYPE html>
<html lang="en">
<head>
<meta charset="utf-8">
<title>Trevanix — Business Card</title>
<link rel="stylesheet" href="https://fonts.googleapis.com/css2?family=Lato:wght@300;400;700&display=swap">
<style>
  :root {
    --backdrop: #e8e6e3;
    --card-white: #ffffff;
    --graphite: #27292b;
    --graphite-soft: #3a3c3f;
    --cyan: #1fb8dc;
    --cyan-light: #2ecbe9;
    --text-light: #f2f2f2;
    --text-muted: #b9bcc0;
    --logo-ink: #2b2c2e;
  }
  * { box-sizing: border-box; margin: 0; padding: 0; }
  html, body {
    width: 1200px; height: 750px; overflow: hidden;
    background: var(--backdrop);
    font-family: "Lato", Arial, sans-serif;
  }
  .canvas {
    position: relative; width: 1200px; height: 750px;
    display: flex; align-items: center; justify-content: center; gap: 50px;
  }
  .card {
    position: relative; width: 525px; height: 300px;
    background: var(--card-white); overflow: hidden;
    box-shadow: 0 6px 18px rgba(0,0,0,0.18);
  }
  .card-shapes { position: absolute; inset: 0; width: 100%; height: 100%; }

  /* Front */
  .contact-block {
    position: absolute; left: 34px; top: 34px; width: 200px; color: var(--text-light);
  }
  .person-name { font-weight: 700; font-size: 17px; letter-spacing: 0.2px; }
  .person-title { font-size: 12px; color: var(--text-muted); margin-top: 2px; }
  .contact-list { list-style: none; margin-top: 22px; font-size: 12.5px; line-height: 20px; }
  .contact-list li { display: flex; align-items: center; gap: 7px; }
  .contact-list .no-icon { padding-left: 19px; }
  .contact-icon { width: 12px; height: 12px; flex: none; }

  .brand {
    position: absolute; display: flex; align-items: center;
  }
  .brand-mark { background: var(--cyan); flex: none; }
  .brand-name { font-weight: 300; color: var(--logo-ink); letter-spacing: 0.5px; }
  .card-front .brand { left: 290px; top: 100px; gap: 10px; }
  .card-front .brand-mark { width: 24px; height: 24px; }
  .card-front .brand-name { font-size: 30px; }

  /* Back */
  .card-back .brand { left: 70px; top: 70px; gap: 18px; }
  .card-back .brand-mark { width: 56px; height: 56px; }
  .card-back .brand-name { font-size: 64px; }
  .web-band {
    position: absolute; left: 0; right: 0; top: 190px; height: 34px;
    background: var(--graphite);
    display: flex; align-items: center; justify-content: center;
    color: #ffffff; font-weight: 700; font-size: 16px; letter-spacing: 0.3px;
  }
</style>
</head>
<body>
<main class="canvas">

  <section class="card card-front" aria-label="Business card, front">
    <svg class="card-shapes" viewBox="0 0 525 300" aria-hidden="true">
      <rect class="panel-dark" x="0" y="0" width="240" height="300" fill="var(--graphite)"/>
      <polygon class="accent-top" points="0,0 110,0 0,32" fill="var(--cyan-light)"/>
      <polygon class="wedge-right" points="455,190 525,142 525,168" fill="var(--graphite-soft)"/>
      <polygon class="band-cyan" points="120,300 525,168 525,246 420,300" fill="var(--cyan)"/>
      <polygon class="corner-dark" points="420,300 525,246 525,300" fill="var(--graphite)"/>
    </svg>

    <div class="contact-block">
      <p class="person-name">Drobyshev Kirill, PMP</p>
      <p class="person-title">Partner</p>
      <ul class="contact-list">
        <li class="no-icon">Beregovaya 7/2</li>
        <li class="no-icon">Moscow, Russia, 117342</li>
        <li>
          <svg class="contact-icon" viewBox="0 0 12 12" aria-hidden="true">
            <path d="M1 4 Q6 0 11 4 L9.5 5.5 L8 4.3 L4 4.3 L2.5 5.5 Z M3 6 H9 L10 11 H2 Z" fill="var(--text-muted)"/>
          </svg>
          +7 (915) 460 7185
        </li>
        <li>
          <svg class="contact-icon" viewBox="0 0 12 12" aria-hidden="true">
            <rect x="0.5" y="2.5" width="11" height="7.5" fill="none" stroke="var(--text-muted)"/>
            <path d="M0.5 2.5 L6 7 L11.5 2.5" fill="none" stroke="var(--text-muted)"/>
          </svg>
          info@trevanix.ru
        </li>
      </ul>
    </div>

    <div class="brand">
      <span class="brand-mark"></span>
      <span class="brand-name">Trevanix</span>
    </div>
  </section>

  <section class="card card-back" aria-label="Business card, back">
    <div class="brand">
      <span class="brand-mark"></span>
      <span class="brand-name">Trevanix</span>
    </div>
    <div class="web-band">www.trevanix.ru</div>
  </section>

</main>
</body>
</html>
```